Natural Skin Care e commerce website

we are the distributor for natural skincare product , we would like to develop a e commerce website which encompass the ability to divide the product into face, body , baby , and base on ingredient , best seller, we are Olvexa certified product the key point to focus is natural organic , no nasties, vegan , unpolluted , full of natural ingredient. manuka, olive nordic style temporary style website is preferred. the website name is Quillom store.co , the web must have ability to take the order and let the brand upload their products

```html
<!DOCTYPE html>
<html lang="en">
<head>
<meta charset="utf-8">
<title>Quillom store.co — Natural, Organic and Vegan Skin Care</title>
<link href="https://fonts.googleapis.com/css2?family=Josefin+Sans:wght@300;400;600&family=Lato:wght@400;700&display=swap" rel="stylesheet">
<style>
:root{
  --pink:#dc4767;
  --green:#1d9a4b;
  --leaf:#8fbf7a;
  --ink:#333333;
  --soft:#f3f3f3;
  --card:#f8f8f8;
  --dark:#1c1a1b;
  --white:#ffffff;
}
*{box-sizing:border-box;margin:0;padding:0}
html,body{width:1200px;height:4453px;overflow:hidden;background:var(--white)}
body{position:relative;font-family:"Lato",sans-serif;color:var(--ink)}
.abs{position:absolute}
a{color:inherit;text-decoration:none}
.heading{font-family:"Josefin Sans",sans-serif;font-weight:300;letter-spacing:3px;color:#222;text-transform:uppercase}
.btn{position:absolute;background:var(--pink);color:var(--white);font-weight:700;font-size:16px;display:flex;align-items:center;justify-content:center;border-radius:4px 18px 4px 18px}
.btn::before{content:"";position:absolute;left:10px;top:-3px;width:11px;height:8px;border-radius:0 8px 0 8px;background:var(--green)}

/* header */
.logo{left:88px;top:14px;width:160px;text-align:center;font-family:"Josefin Sans",sans-serif;font-weight:400;color:var(--green);font-size:32px;letter-spacing:5px}
.logo .dot{display:block;width:40px;height:40px;border-radius:50%;background:var(--pink);margin:0 auto 12px}
.icons{left:960px;top:26px;display:flex;gap:9px}
.icons span{width:44px;height:44px;border-radius:50%;background:var(--pink);display:flex;align-items:center;justify-content:center}
.nav{left:411px;top:102px;display:flex;gap:44px;font-size:15px;letter-spacing:1.4px;font-family:"Josefin Sans",sans-serif;color:#222}
.nav .on{color:var(--pink)}

/* hero */
.hero-img{left:0;top:133px;width:1200px;height:660px;
  background:
    radial-gradient(ellipse 260px 200px at 70px 300px,rgba(143,191,122,.55),rgba(143,191,122,0) 70%),
    radial-gradient(ellipse 200px 150px at 90px 640px,rgba(143,191,122,.45),rgba(143,191,122,0) 70%),
    radial-gradient(ellipse 260px 300px at 830px 360px,#e7b9a0 0%,rgba(231,185,160,0) 75%),
    radial-gradient(ellipse 140px 130px at 865px 340px,#f4eeee 0%,rgba(244,238,238,0) 80%),
    radial-gradient(ellipse 260px 140px at 850px 40px,#e9ecef 0%,rgba(233,236,239,0) 75%),
    linear-gradient(100deg,#bcd4e6 0%,#d8e6ee 38%,#e9d3c6 58%,#d9ad94 82%,#c99a83 100%)}
.hero-copy{left:80px;top:283px;width:500px;text-align:center}
.hero-copy .mark{width:78px;height:78px;border-radius:50%;background:var(--pink);margin:0 auto 22px}
.hero-copy .name{font-family:"Josefin Sans",sans-serif;font-size:62px;color:var(--green);letter-spacing:7px;line-height:1}
.hero-copy p{font-size:19px;line-height:33px;color:#333;margin-top:26px}

/* categories */
.grid{left:117px;top:1023px;width:966px;height:506px;display:grid;grid-template-columns:repeat(3,322px);grid-template-rows:253px 253px;box-shadow:0 4px 18px rgba(0,0,0,.08)}
.cell{position:relative;text-align:center;padding-top:52px}
.cell h3{font-family:"Josefin Sans",sans-serif;font-weight:400;font-size:26px;color:var(--pink)}
.cell p{font-size:15.5px;line-height:30px;margin:16px auto 0;width:290px;color:#444}
.cell a{display:inline-block;margin-top:16px;font-size:15px;font-weight:700;color:var(--pink);text-decoration:underline}
.cell.light{background:var(--card)}
.cell.pinked{background:var(--pink)}
.cell.pinked h3,.cell.pinked p,.cell.pinked a{color:var(--white)}
.ph{padding:0}
.tri{position:absolute;left:152px;top:0;width:0;height:0;border-left:9px solid transparent;border-right:9px solid transparent;border-top:10px solid var(--pink)}

/* about */
.about-bg{left:0;top:1700px;width:1200px;height:575px;background:var(--soft)}
.about-text{left:90px;top:1862px;width:425px;font-size:14.5px;line-height:33px;color:#333;text-align:justify}
.about-img{left:595px;top:1735px;width:550px;height:540px;border-radius:48% 48% 30% 40%;
  background:
    radial-gradient(circle 130px at 200px 140px,#f5f1ec 0%,#e7e2dc 80%,rgba(231,226,220,0) 100%),
    radial-gradient(circle 130px at 150px 380px,#f1ece7 0%,#e2dcd6 80%,rgba(226,220,214,0) 100%),
    radial-gradient(circle 130px at 390px 310px,#f1d3d8 0%,#e4bcc3 80%,rgba(228,188,195,0) 100%),
    linear-gradient(160deg,#f3f3f3,#e9e9e9)}
.badge{left:985px;top:1815px;width:100px;height:100px;border-radius:50%;border:3px solid var(--green);background:var(--white)}

/* products */
.card{top:2503px;width:237px;height:312px;background:var(--white);box-shadow:0 2px 14px rgba(0,0,0,.09);text-align:center}
.card .shot{margin:24px auto 0;width:78px;height:180px;background:linear-gradient(90deg,#e4e4e4,#fafafa 45%,#dcdcdc);border-radius:18px 18px 8px 8px}
.card .shot.jar{width:210px;height:130px;margin-top:52px;border-radius:12px;background:linear-gradient(100deg,#6a6a3a 0%,#bcb89a 30%,#f6f3ee 55%,#b9b9b9 100%)}
.card .pn{font-family:"Josefin Sans",sans-serif;font-size:19px;color:#444;margin-top:24px}
.card .shot.jar + .pn{margin-top:22px}
.card .pr{color:var(--pink);font-size:17px;margin-top:12px}
.arrow{top:2638px;width:40px;height:40px;border-radius:50%;border:1px solid #ddd;display:flex;align-items:center;justify-content:center}

/* love */
.love-img{left:0;top:2930px;width:1200px;height:610px;
  background:
    radial-gradient(ellipse 300px 360px at 330px 300px,#e8c8b4 0%,rgba(232,200,180,0) 75%),
    radial-gradient(ellipse 200px 140px at 120px 90px,#f4f2f0 0%,rgba(244,242,240,0) 80%),
    radial-gradient(ellipse 110px 90px at 640px 440px,#eeeeee 0%,rgba(238,238,238,0) 80%),
    linear-gradient(90deg,#e2c3b1 0%,#ecd8cb 35%,#f3efec 55%,#f7f7f7 100%)}
.love-text{left:680px;top:3098px;width:425px;font-size:14.5px;line-height:33px;color:#333;text-align:justify}

/* newsletter */
.news-img{left:950px;top:3505px;width:420px;height:420px;border-radius:50%;background:radial-gradient(circle at 42% 50%,#f8dce2 0%,#e39aab 28%,#c76e85 40%,#cfc8ca 58%,#ecebeb 78%,#bdbdbd 100%)}
.news-text{left:260px;top:3748px;width:680px;text-align:center;font-size:15.5px;line-height:31px;color:#444}
.field{left:282px;top:3840px;width:633px;height:50px;background:#efefef;border-radius:4px 22px 4px 22px;font-size:14px;color:#666;padding:17px 0 0 32px}

/* footer */
.footer{left:0;top:4065px;width:1200px;height:388px;background:var(--dark);color:#eee}
.fcol{position:absolute;top:68px}
.fcol h4{font-family:"Josefin Sans",sans-serif;font-weight:400;font-size:18px;letter-spacing:1.5px;margin-bottom:24px}
.fcol li{list-style:none;font-size:13px;line-height:31px}
.social{display:flex;gap:22px;margin-top:4px}
.social span{width:14px;height:14px;border-radius:50%;background:#eee}
.cards{left:522px;top:4380px;display:flex;gap:6px}
.cards span{width:34px;height:20px;border-radius:3px}
.cards span:nth-child(1){background:#e4a14a}.cards span:nth-child(2){background:#3e66b8}.cards span:nth-child(3){background:#5aa8d8}.cards span:nth-child(4){background:#d9d9d9}
.copy{left:0;top:4418px;width:1200px;text-align:center;font-size:11px;color:#ddd}
</style>
</head>
<body>

<header>
  <div class="abs logo"><span class="dot"></span>QUILLOM</div>
  <div class="abs icons">
    <span><svg width="16" height="16" viewBox="0 0 24 24"><path d="M12 21l-8-8a5 5 0 017-7l1 1 1-1a5 5 0 017 7z" fill="#fff"/></svg></span>
    <span><svg width="16" height="16" viewBox="0 0 24 24"><path d="M3 4h3l2 11h11l2-8H7" stroke="#fff" stroke-width="2.4" fill="none"/><circle cx="9" cy="19" r="1.8" fill="#fff"/><circle cx="17" cy="19" r="1.8" fill="#fff"/></svg></span>
    <span><svg width="16" height="16" viewBox="0 0 24 24"><circle cx="10" cy="10" r="6" stroke="#fff" stroke-width="2.6" fill="none"/><path d="M15 15l6 6" stroke="#fff" stroke-width="2.6"/></svg></span>
  </div>
  <nav class="abs nav">
    <a class="on">HOME</a><a>ABOUT US</a><a>PRODUCTS</a><a>CATEGORIES</a><a>BLOG</a><a>CONTACT US</a>
  </nav>
</header>

<section class="hero">
  <div class="abs hero-img" role="img" aria-label="Smiling woman in a white towel holding a jar of natural organic cream over one eye, green leaves on a soft blue background"></div>
  <svg class="abs" style="left:0;top:690px" width="1200" height="110" viewBox="0 0 1200 110">
    <path d="M0 50 C120 70 260 90 380 70 C420 60 430 52 440 48 C480 70 520 90 600 86 C800 75 1000 20 1200 0 L1200 110 L0 110Z" fill="#fff"/>
    <path d="M0 50 C120 70 260 90 380 70 C420 60 430 52 440 48 C480 70 520 90 600 86 C800 75 1000 20 1200 0" stroke="var(--pink)" stroke-width="5" fill="none"/>
  </svg>
  <div class="abs hero-copy">
    <div class="mark"></div>
    <div class="name">QUILLOM</div>
    <p>Lorem ipsum dolor sit amet, consectetur adipiscing elit,<br>ed do eiusmod tempo</p>
  </div>
  <a class="btn" style="left:252px;top:600px;width:156px;height:48px">Buy Now</a>
</section>

<section class="categories">
  <h2 class="abs heading" style="left:0;top:935px;width:1200px;text-align:center;font-size:44px">Categories</h2>
  <div class="abs grid">
    <div class="cell light"><h3>Baby</h3><p>Lorem ipsum dolor sit amet, turing elit, sed do eiusmod tempor incididunt</p><a>Buy Now →</a></div>
    <div class="cell ph" role="img" aria-label="Woman applying a natural green clay face mask" style="background:radial-gradient(ellipse 110px 120px at 150px 120px,#d9c2b0,rgba(217,194,176,0) 80%),linear-gradient(135deg,#d5d2cd,#b3aaa2)"></div>
    <div class="cell light"><h3>Body</h3><p>Lorem ipsum dolor sit amet, turing elit, sed do eiusmod tempor incididunt</p><a>Buy Now →</a></div>
    <div class="cell ph" role="img" aria-label="Hands gently massaging a baby's feet with vegan baby lotion" style="background:radial-gradient(ellipse 130px 110px at 180px 110px,#e8c7b8,rgba(232,199,184,0) 80%),linear-gradient(135deg,#eee5e1,#c9aea4)"><span class="tri"></span></div>
    <div class="cell pinked"><h3>Face</h3><p>Lorem ipsum dolor sit amet, turing elit, sed do eiusmod tempor incididunt</p><a>Buy Now →</a></div>
    <div class="cell ph" role="img" aria-label="Hand smoothing organic body lotion onto an arm" style="background:radial-gradient(ellipse 150px 110px at 190px 130px,#ebcdb9,rgba(235,205,185,0) 80%),linear-gradient(135deg,#f6f4f2,#eadbd0)"><span class="tri"></span></div>
  </div>
</section>

<section class="about">
  <svg class="abs" style="left:0;top:1610px" width="1200" height="92" viewBox="0 0 1200 92">
    <path d="M0 92 L0 80 C200 70 420 20 600 12 C700 8 760 30 795 45 C900 10 1050 15 1200 50 L1200 92Z" fill="var(--soft)"/>
    <path d="M100 80 C300 60 440 18 600 12 C700 8 760 30 795 45 C900 10 1050 15 1200 50" stroke="var(--pink)" stroke-width="5" fill="none"/>
  </svg>
  <div class="abs about-bg"></div>
  <h2 class="abs heading" style="left:90px;top:1793px;font-size:44px">About Us</h2>
  <p class="abs about-text">Lorem ipsum dolor sit amet, consectetur adipiscing elit, sed do eiusmod tempor incididunt ut labore et dolore magna aliqua. Ut enim ad minim veniam, quis nostrudtion ullamco laboris nisi ut aliquip ex ea commodo consequat. Duis aute irure dolor in reprehenderit in voluptate velit esse cillum dolore eu fugiat nulla pariatur. Excepteur sint cat cupidatat non proident, in culpa qui officiarunt mollit anim id est laborum.</p>
  <a class="btn" style="left:90px;top:2113px;width:158px;height:48px">Read More</a>
  <div class="abs about-img" role="img" aria-label="Three open jars of white and pink natural vegan cream"></div>
  <div class="abs badge" role="img" aria-label="Natural ingredients badge"></div>
</section>

<section class="products">
  <h2 class="abs heading" style="left:0;top:2423px;width:1200px;text-align:center;font-size:44px">Our Products</h2>
  <div class="abs arrow" style="left:23px"><svg width="10" height="14"><path d="M8 1L2 7l6 6" stroke="var(--pink)" stroke-width="2" fill="none"/></svg></div>
  <div class="abs arrow" style="left:1135px"><svg width="10" height="14"><path d="M2 1l6 6-6 6" stroke="#bbb" stroke-width="2" fill="none"/></svg></div>
  <div class="abs card" style="left:90px"><div class="shot" role="img" aria-label="White lotion bottle"></div><div class="pn">Product Name</div><div class="pr">$21.00</div></div>
  <div class="abs card" style="left:351px;box-shadow:0 4px 26px rgba(220,71,103,.25)"><div class="shot jar" role="img" aria-label="Open cream jar with olives and olive leaves"></div><div class="pn">Product Name</div><div class="pr">$21.00</div></div>
  <div class="abs card" style="left:612px"><div class="shot" role="img" aria-label="White cream tube" style="width:84px;border-radius:6px 6px 14px 14px"></div><div class="pn">Product Name</div><div class="pr">$21.00</div></div>
  <div class="abs card" style="left:873px"><div class="shot" role="img" aria-label="White lotion bottle"></div><div class="pn">Product Name</div><div class="pr">$21.00</div></div>
  <a class="btn" style="left:138px;top:2793px;width:140px;height:48px">Read More</a>
  <a class="btn" style="left:400px;top:2793px;width:140px;height:48px">Read More</a>
  <a class="btn" style="left:661px;top:2793px;width:140px;height:48px">Read More</a>
  <a class="btn" style="left:922px;top:2793px;width:140px;height:48px">Read More</a>
</section>

<section class="love">
  <div class="abs love-img" role="img" aria-label="Woman in a towel dabbing her cheek with a cotton pad beside a jar of organic cream"></div>
  <svg class="abs" style="left:0;top:3440px" width="1200" height="110" viewBox="0 0 1200 110">
    <path d="M0 60 C150 90 320 95 420 72 C440 68 445 66 450 64 C480 85 520 90 600 80 C800 50 1000 20 1200 15 L1200 110 L0 110Z" fill="#fff"/>
    <path d="M0 60 C150 90 320 95 420 72 C440 68 445 66 450 64 C480 85 520 90 600 80 C800 50 1000 20 1200 15" stroke="var(--pink)" stroke-width="5" fill="none"/>
  </svg>
  <h2 class="abs heading" style="left:677px;top:3048px;font-size:44px">Love Your Skin</h2>
  <p class="abs love-text">Lorem ipsum dolor sit amet, consectetur adipiscing elit, sed do eiusmod tempor incididunt ut labore et dolore magna aliqua. Ut enim ad minim veniam, quis nostrudtion ullamco laboris nisi ut aliquip ex ea commodo consequat. Duis aute irure dolor in reprehenderit in voluptate velit esse cillum dolore eu fugiat nulla pariatur.</p>
  <a class="btn" style="left:682px;top:3333px;width:156px;height:48px">Buy Now</a>
</section>

<section class="newsletter">
  <div class="abs news-img" role="img" aria-label="Close view of an open jar of pink natural cream"></div>
  <h2 class="abs heading" style="left:0;top:3682px;width:1200px;text-align:center;font-size:44px">Join Our Newsletter</h2>
  <p class="abs news-text">Lorem ipsum dolor sit amet, consectetur adipiscing elit, sed do eiusmod tempor incididunt magna aliqua. Ut enim ad minim veniam, quis nostrud exercitation ullamco</p>
  <div class="abs field">Enter Your Email Address</div>
  <a class="btn" style="left:767px;top:3840px;width:148px;height:50px">Join Now</a>
</section>

<footer>
  <svg class="abs" style="left:0;top:3975px" width="1200" height="95" viewBox="0 0 1200 95">
    <path d="M0 70 C150 60 350 50 520 30 C560 25 590 22 610 28 C640 45 680 55 760 52 C950 45 1100 55 1200 65 L1200 95 L0 95Z" fill="var(--dark)"/>
    <path d="M0 70 C150 60 350 50 520 30 C560 25 590 22 610 28 C640 45 680 55 760 52 C950 45 1100 55 1200 65" stroke="var(--pink)" stroke-width="6" fill="none"/>
  </svg>
  <div class="abs footer">
    <div class="fcol" style="left:104px"><h4>COMPANY</h4><ul><li>Home</li><li>About Us</li><li>Products</li><li>Categories</li><li>Blog</li><li>Contact Us</li></ul></div>
    <div class="fcol" style="left:357px"><h4>CONTACT US</h4><ul><li>+0 123 456 7890</li><li>hello@quillomstore.co</li></ul></div>
    <div class="fcol" style="left:620px"><h4>CATEGORIES</h4><ul><li>Face</li><li>Baby</li><li>Body</li></ul></div>
    <div class="fcol" style="left:928px"><h4>MY ACCOUNT</h4><ul><li>Log in</li><li>My Account</li></ul>
      <h4 style="margin-top:38px;margin-bottom:18px">FOLLOW US</h4>
      <div class="social" aria-label="Social links"><span></span><span></span><span></span><span></span><span></span></div>
    </div>
  </div>
  <div class="abs cards" aria-label="Accepted payment cards"><span></span><span></span><span></span><span></span></div>
  <p class="abs copy">© 2020 The Company Name. All rights Reserved.Privacy Policy | Terms Of Use</p>
</footer>

</body>
</html>
```